'Brantley e@sy' Initial leaflet

I need an A5 Leaflet designed to launch the new service we are offering.
Currently we operate a traditional estate agency based in the uk that covers sales and letting of property.

The working name for the new service is 'Brantley e@sy'

We are starting a new offering that will be an online offering for the local area. Similar to 'Tallowgate' but with an actual local face and office.
I need the leaflet to promote this.
The leaflet must be modern, informative and in our corporate colours. I have attached some logos and previous leaflets that we have had to show colours etc.
The main points to detail on the leaflet will be that
we offer an Online Service
Its a lower price
We still offer the local office/face.
Professional Photos Included
Floorplans Included

The price we will offer this service at will be 'From £795 inc VAT'

Id like to have an offer on the leaflet that instruction received in September/October 2018 will get the service for reduced price of £600 Including VAT.

I look forward to seeing what we get!

Martin

Requirements
Must have
• Must be double sided! Should be attractive and modern.

```html
<!DOCTYPE html>
<html lang="en">
<head>
<meta charset="utf-8">
<title>Brantley e@sy – Leaflet</title>
<link rel="stylesheet" href="https://fonts.googleapis.com/css2?family=Montserrat:wght@300;400;500;600;700;800&family=Open+Sans:wght@400;600&display=swap">
<style>
:root{
  --orange:#f04e30;
  --black:#000;
  --white:#fff;
  --stage:#dedede;
  --ink:#222;
  --green-1:#8fb46a;
  --green-2:#4d7a3a;
  --sky:#dfe9ef;
}
*{margin:0;padding:0;box-sizing:border-box}
html,body{width:1200px;height:871px;overflow:hidden}
body{background:radial-gradient(ellipse at center,#f2f2f2 0%,var(--stage) 100%);font-family:"Open Sans",sans-serif;position:relative}
.page{position:absolute;top:45px;width:517px;height:733px;overflow:hidden;box-shadow:0 4px 14px rgba(0,0,0,.35)}
.page--front{left:56px;background:var(--black)}
.page--back{left:625px;background:var(--white)}
.abs{position:absolute}
.center{left:0;right:0;text-align:center}
.brand-mark{display:flex;align-items:center;gap:10px}
.brand-dot{width:52px;height:52px;border-radius:50%;background:var(--orange)}
.brand-name{font-family:"Montserrat",sans-serif;font-weight:700;color:var(--orange);font-size:40px;line-height:1}
.social{display:flex;gap:9px}
.social span{width:25px;height:25px;background:var(--orange)}
.welcome{font-family:"Montserrat",sans-serif;color:var(--white);font-weight:300;font-size:22px}
.welcome-title{font-family:"Montserrat",sans-serif;color:var(--orange);font-weight:800;font-size:23px}
.intro{font-family:"Montserrat",sans-serif;color:var(--white);font-size:12.2px;line-height:16px;padding:0 40px;letter-spacing:-.2px;text-align:justify;text-align-last:center}
.divider{left:230px;width:57px;height:1px;background:var(--orange)}
.hours{font-family:"Montserrat",sans-serif;color:var(--orange);font-weight:800;font-size:14.5px}
.footer{left:0;bottom:0;width:517px;height:67px}
.footer-address{left:14px;top:6px;font-size:10px;line-height:13px;color:var(--ink)}
.footer-address strong{display:block;color:var(--orange);font-family:"Montserrat",sans-serif;font-weight:800;font-size:10.5px;margin-bottom:1px}
.footer-address .row{display:flex;align-items:center;gap:6px}
.footer-address .row i{width:8px;height:8px;border-radius:50%;background:var(--orange);flex:none}
.phone{font-family:"Montserrat",sans-serif;font-weight:800;font-size:35px;color:var(--white);line-height:1;display:flex;align-items:center;gap:5px}
.web{font-family:"Montserrat",sans-serif;font-weight:600;font-size:15px;color:var(--white);display:flex;align-items:center;gap:8px}
.ring{width:16px;height:16px;border-radius:50%;border:2px solid var(--white);flex:none}
.lead{font-family:"Montserrat",sans-serif;font-size:22px;color:var(--ink)}
.headline{font-family:"Montserrat",sans-serif;font-weight:800;font-size:58px;color:var(--orange);letter-spacing:-.5px;line-height:1}
.sub{font-family:"Montserrat",sans-serif;font-weight:500;font-size:13.5px;line-height:19px;color:var(--ink);padding:0 38px}
.pill{background:var(--orange);color:var(--ink);font-family:"Montserrat",sans-serif;font-weight:700;font-size:20px;height:34px;border-radius:10px;display:flex;align-items:center;justify-content:center;box-shadow:0 2px 3px rgba(0,0,0,.25)}
.point{font-family:"Montserrat",sans-serif;font-weight:700;font-size:20px;color:var(--black)}
.offer{left:44px;top:391px;width:428px;height:111px;border:1.5px dashed var(--orange);border-radius:6px;text-align:center;color:var(--white)}
.offer-intro{font-family:"Montserrat",sans-serif;font-weight:300;font-size:19px;margin-top:8px}
.offer-price{font-family:"Montserrat",sans-serif;font-weight:800;font-size:29px;color:var(--orange);line-height:34px}
.offer-note{font-family:"Montserrat",sans-serif;font-size:11.5px;line-height:16px}
.feature{width:144px;text-align:center;top:522px}
.feature-icon{width:53px;height:53px;border-radius:50%;background:var(--orange);margin:0 auto;display:flex;align-items:center;justify-content:center}
.feature-title{font-family:"Montserrat",sans-serif;font-weight:600;color:var(--orange);font-size:10.2px;margin-top:14px;white-space:nowrap;letter-spacing:-.1px}
.feature-text{font-family:"Open Sans",sans-serif;color:var(--white);font-size:8.7px;line-height:12.6px;margin-top:6px;letter-spacing:-.2px;text-align:justify;text-align-last:center}
.side-label{top:805px;width:200px;font-family:"Montserrat",sans-serif;font-weight:300;font-size:32px;color:#333;text-align:center}
</style>
</head>
<body>

<section class="page page--front">
  <div class="abs brand-mark" style="left:35px;top:21px">
    <span class="brand-dot"></span>
    <span class="brand-name">Brantley</span>
  </div>
  <div class="abs social" style="left:402px;top:36px"><span></span><span></span><span></span></div>

  <svg class="abs" style="left:0;top:0" width="517" height="520" viewBox="0 0 517 520">
    <defs>
      <linearGradient id="scene" x1="0" y1="0" x2="0" y2="1">
        <stop offset="0" stop-color="var(--sky)"/>
        <stop offset=".45" stop-color="var(--green-1)"/>
        <stop offset="1" stop-color="var(--green-2)"/>
      </linearGradient>
      <linearGradient id="house" x1="0" y1="0" x2="0" y2="1">
        <stop offset="0" stop-color="#a9c8e0"/>
        <stop offset=".5" stop-color="#c9b389"/>
        <stop offset="1" stop-color="#5d7f3f"/>
      </linearGradient>
    </defs>
    <path d="M0,227 Q200,70 517,118 L517,330 Q300,410 0,395 Z" fill="url(#scene)" stroke="var(--orange)" stroke-width="7" role="img" aria-label="Photo of a village green with a war memorial and trees"/>
    <circle cx="88" cy="415" r="60" fill="url(#house)" stroke="var(--orange)" stroke-width="5" role="img" aria-label="Photo of a terrace of houses"/>
    <circle cx="268" cy="399" r="60" fill="url(#house)" stroke="var(--orange)" stroke-width="5" role="img" aria-label="Photo of a brick house"/>
    <circle cx="428" cy="335" r="62" fill="url(#house)" stroke="var(--orange)" stroke-width="5" role="img" aria-label="Photo of a bungalow"/>
  </svg>

  <div class="abs center welcome" style="top:472px">Welcome to</div>
  <div class="abs center welcome-title" style="top:497px">BRANTLEY ESTATE AGENTS</div>
  <p class="abs center intro" style="top:537px">Brantley Estate Agents specialise in residential sales, lettings and property management. Our experienced team can advise you on just about everything from decor to financial advice, we have it covered!</p>
  <div class="abs divider" style="top:598px"></div>
  <p class="abs center intro" style="top:609px;font-size:11.8px;line-height:15px;padding:0 75px">Please browse through our website and contact us should you need any further advice or assistance.</p>
  <div class="abs center hours" style="top:643px">Phone lines are open 8am to 9pm, 7 days a week!</div>

  <div class="abs footer">
    <svg class="abs" width="517" height="67" viewBox="0 0 517 67">
      <rect width="517" height="67" fill="var(--white)"/>
      <polygon points="208,0 517,0 517,67 228,67" fill="var(--orange)"/>
      <polygon points="200,0 208,0 228,67 220,67" fill="var(--black)"/>
    </svg>
    <div class="abs footer-address">
      <strong>BRANTLEY ESTATE AGENTS</strong>
      <div class="row"><i></i><span>14 Mill Lane, Ashwick,<br>Hertfordshire, AB1 2CD</span></div>
      <div class="row"><i></i><span>info@brantleyestateagents.co.uk</span></div>
    </div>
    <div class="abs phone" style="left:226px;top:6px"><span class="ring"></span>01632 960500</div>
    <div class="abs web" style="left:229px;top:44px"><span class="ring" style="width:14px;height:14px"></span>www.brantleyestateagents.co.uk</div>
  </div>
</section>

<section class="page page--back">
  <svg class="abs" style="left:0;top:0" width="517" height="733" viewBox="0 0 517 733">
    <defs>
      <linearGradient id="trees" x1="1" y1="0" x2="0" y2="0">
        <stop offset="0" stop-color="var(--green-1)" stop-opacity=".7"/>
        <stop offset="1" stop-color="var(--green-1)" stop-opacity="0"/>
      </linearGradient>
    </defs>
    <path d="M200,330 Q360,290 517,250 L517,320 Q300,400 200,360 Z" fill="url(#trees)" role="img" aria-label="Faded photo of wooded countryside"/>
    <path d="M0,282 Q250,440 517,312 L517,733 L0,733 Z" fill="var(--black)"/>
    <path d="M0,282 Q250,440 517,312" fill="none" stroke="var(--orange)" stroke-width="7"/>
  </svg>

  <div class="abs center lead" style="top:20px">Our new service is</div>
  <div class="abs center headline" style="top:56px">Brantley e@sy</div>
  <p class="abs center sub" style="top:128px">We are starting a new offering that will be an online offering for the local area</p>

  <div class="abs pill" style="left:102px;top:167px;width:314px">We offer an Online Service</div>
  <div class="abs center point" style="top:206px">Its a lower price</div>
  <div class="abs pill" style="left:68px;top:236px;width:380px">We still offer the local office/face.</div>
  <div class="abs center point" style="top:275px">Professional Photos Included</div>
  <div class="abs pill" style="left:141px;top:305px;width:234px">Floorplans Included</div>

  <div class="abs offer">
    <div class="offer-intro">The price we will offer this service at will be</div>
    <div class="offer-price">'From £795 inc VAT'</div>
    <div class="offer-note">instruction received in September/October 2018 will get the<br>service for reduced price of £600 Including VAT</div>
  </div>

  <div class="abs feature" style="left:26px">
    <div class="feature-icon">
      <svg width="30" height="28" viewBox="0 0 30 28"><path d="M15 2 L28 14 L24 14 L24 26 L18 26 L18 18 L12 18 L12 26 L6 26 L6 14 L2 14 Z" fill="var(--white)"/></svg>
    </div>
    <div class="feature-title">What's Your Home Worth?</div>
    <div class="feature-text">Try our instant online valuation tool and find out what your home could be worth in as little as 60 seconds.</div>
  </div>
  <div class="abs feature" style="left:182px">
    <div class="feature-icon">
      <svg width="28" height="28" viewBox="0 0 28 28"><path d="M19 3 L25 9 L11 23 L4 25 L6 18 Z" fill="var(--white)"/><path d="M16 6 L22 12" stroke="var(--orange)" stroke-width="2"/></svg>
    </div>
    <div class="feature-title">Register With Us</div>
    <div class="feature-text">Want to stay up to date with properties you might be interested in? Register with us to receive regular property updates</div>
  </div>
  <div class="abs feature" style="left:345px;top:518px">
    <div class="feature-icon" style="width:56px;height:56px">
      <svg width="30" height="30" viewBox="0 0 30 30"><circle cx="15" cy="10" r="6" fill="var(--white)"/><path d="M4 27 Q4 18 15 18 Q26 18 26 27 Z" fill="var(--white)"/></svg>
    </div>
    <div class="feature-title">Ask an Expert</div>
    <div class="feature-text">Do you have a property related question? Click here to ask your local expert!</div>
  </div>

  <div class="abs footer">
    <svg class="abs" width="517" height="67" viewBox="0 0 517 67">
      <rect width="517" height="67" fill="var(--white)"/>
      <polygon points="207,0 517,0 517,67 227,67" fill="var(--orange)"/>
      <polygon points="199,0 207,0 227,67 219,67" fill="var(--black)"/>
    </svg>
    <div class="abs brand-mark" style="left:18px;top:14px;gap:8px">
      <span class="brand-dot" style="width:40px;height:40px"></span>
      <span class="brand-name" style="font-size:30px">Brantley</span>
    </div>
    <div class="abs phone" style="left:226px;top:6px"><span class="ring"></span>01632 960500</div>
    <div class="abs web" style="left:229px;top:44px"><span class="ring" style="width:14px;height:14px"></span>www.brantleyestateagents.co.uk</div>
  </div>
</section>

<div class="abs side-label" style="left:214px">FRONT</div>
<div class="abs side-label" style="left:793px">BACK</div>

</body>
</html>
```